Business Card design for Brightvale Global

we need a business card design for our company. we are a trading company based in LA.

Company Name: Brightvale Global Corp.
Contact: Marcus Ortega
Title: CEO
Tel: 310-647-2093
Email: bvgcorp7@mailnest.example

Target Market(s)

International, especially China

Industry/Entity Type

Trade

Colors
3276b5
34a7d8
0555a3
0493ce
85cae6
85acd3
d0dfed
cee9f5

Requirements
Must have
• Logo and contact, to have international/global feeling

```html
<!DOCTYPE html>
<html lang="en">
<head>
<meta charset="utf-8">
<title>Brightvale Global – Business Card</title>
<link href="https://fonts.googleapis.com/css2?family=Open+Sans:wght@400;600;700&display=swap" rel="stylesheet">
<style>
  :root {
    --backdrop: #d9d6d2;
    --card-top: #eeebe8;
    --card-bottom: #dedad6;
    --brand-blue: #0555a3;
    --deep-navy: #13365f;
    --ink: #1b2a3d;
    --rule: #4a4f57;
    --band: #1d4a80;
  }
  * { box-sizing: border-box; margin: 0; padding: 0; }
  html, body {
    width: 1200px;
    height: 969px;
    overflow: hidden;
    background: var(--backdrop);
    font-family: "Open Sans", Arial, sans-serif;
  }
  .canvas {
    position: relative;
    width: 1200px;
    height: 969px;
  }
  .card {
    position: absolute;
    left: 165px;
    top: 237px;
    width: 870px;
    height: 495px;
    border-radius: 22px;
    background: linear-gradient(160deg, var(--card-top), var(--card-bottom));
    box-shadow: 0 14px 40px rgba(0, 0, 0, 0.18);
    overflow: hidden;
    text-align: center;
    color: var(--ink);
  }
  .brand {
    position: absolute;
    top: 118px;
    left: 0;
    right: 0;
    display: flex;
    align-items: center;
    justify-content: center;
    gap: 18px;
  }
  .brand-dot {
    width: 64px;
    height: 64px;
    border-radius: 50%;
    background: var(--brand-blue);
  }
  .brand-name {
    font-size: 58px;
    font-weight: 600;
    color: var(--brand-blue);
    letter-spacing: -0.5px;
    line-height: 1;
  }
  .person-name {
    position: absolute;
    top: 274px;
    left: 0;
    right: 0;
    font-size: 29px;
    font-weight: 700;
    color: var(--deep-navy);
    letter-spacing: 0.5px;
  }
  .person-title {
    position: absolute;
    top: 313px;
    left: 0;
    right: 0;
    font-size: 21px;
    font-weight: 700;
    color: var(--deep-navy);
  }
  .contact-block {
    position: absolute;
    top: 358px;
    left: 50%;
    width: 460px;
    margin-left: -230px;
    height: 45px;
    border-top: 1.5px solid var(--rule);
    border-bottom: 1.5px solid var(--rule);
    display: flex;
    align-items: center;
    justify-content: center;
    font-size: 20px;
    color: var(--ink);
    white-space: nowrap;
  }
  .contact-label {
    font-weight: 700;
    color: var(--deep-navy);
    margin-right: 4px;
  }
  .contact-item + .contact-item { margin-left: 10px; }
  .website {
    position: absolute;
    top: 417px;
    left: 0;
    right: 0;
    font-size: 20px;
    font-weight: 700;
    color: var(--deep-navy);
    letter-spacing: 0.8px;
  }
  .bottom-band {
    position: absolute;
    left: 0;
    right: 0;
    bottom: 0;
    height: 19px;
    background: var(--band);
  }
</style>
</head>
<body>
<div class="canvas">
  <div class="card">
    <div class="brand">
      <span class="brand-dot"></span>
      <span class="brand-name">Brightvale Global</span>
    </div>
    <div class="person-name">MARCUS ORTEGA</div>
    <div class="person-title">CEO</div>
    <div class="contact-block">
      <span class="contact-item"><span class="contact-label">P.</span>310-647-2093</span>
      <span class="contact-item"><span class="contact-label">E.</span>bvgcorp7@mailnest.example</span>
    </div>
    <div class="website">WWW.BRIGHTVALE.EXAMPLE</div>
    <div class="bottom-band"></div>
  </div>
</div>
</body>
</html>
```